Business card design needed

I need a business card design for a dog walking, dog minding and dog training business. Please refer to my website for the basic company colours and fonts I'm after. Planning on a double sided card, so all information doesn't need to be on the 'front' side.
Cheers

Industry/Entity Type

Dog Training

Contact Information for Business Card

Meadow Paws - happy hounds
Rua 0498307164
meadowpawsdemo.com.au
-walking
-holiday stays
-onsite care
-training and behavioural consultations

```html
<!DOCTYPE html>
<html lang="en">
<head>
<meta charset="utf-8">
<title>Meadow Paws – Business Cards</title>
<link href="https://fonts.googleapis.com/css2?family=Arvo&family=Michroma&family=Questrial&display=swap" rel="stylesheet">
<style>
  :root {
    --stage: #2b2b2b;
    --card-dark: #0b0b0b;
    --card-dark-glow: #1e1e1e;
    --card-light: #ffffff;
    --orange: #e2622a;
    --grey: #6a6a6a;
    --grey-light: #8a8a8a;
    --white: #ffffff;
  }
  * { margin: 0; padding: 0; box-sizing: border-box; }
  html, body { width: 1200px; height: 1200px; overflow: hidden; }
  body { background: var(--stage); position: relative; font-family: "Questrial", sans-serif; }

  .card { position: absolute; left: 270px; width: 666px; height: 362px; overflow: hidden; }
  .card--dark { background: radial-gradient(ellipse at 50% 35%, var(--card-dark-glow) 0%, var(--card-dark) 70%); }
  .card--front { top: 26px; }
  .card--plain { top: 419px; }
  .card--back { top: 812px; height: 363px; background: var(--card-light); }

  .wordmark { position: absolute; font-family: "Arvo", serif; color: var(--orange); white-space: nowrap; line-height: 1; }
  .card--dark .wordmark { right: 96px; top: 128px; font-size: 58px; }
  .card--back .wordmark { left: 15px; top: 20px; font-size: 36px; }

  .tagline { position: absolute; font-family: "Michroma", sans-serif; color: var(--orange); white-space: nowrap; line-height: 1; }
  .card--dark .tagline { right: 96px; top: 196px; font-size: 11px; letter-spacing: 2.5px; }
  .card--back .tagline { right: 354px; top: 62px; font-size: 9px; letter-spacing: 2px; }

  .web-band { position: absolute; right: 0; bottom: 0; width: 254px; height: 25px; background: var(--orange);
    color: var(--white); font-family: "Michroma", sans-serif; font-size: 7.5px; letter-spacing: 1.1px;
    display: flex; align-items: center; justify-content: center; white-space: nowrap; overflow: hidden; }

  .puppy-photo { position: absolute; right: 0; top: 270px; width: 120px; height: 67px;
    background: linear-gradient(180deg, #b8642c 0%, #efe6dc 60%, #f5f1ea 100%); border-radius: 50px 50px 6px 6px; }

  .pointer { position: absolute; left: 0; top: 166px; }
  .contact-name { position: absolute; left: 48px; top: 164px; font-size: 38px; color: var(--grey-light); line-height: 1; }
  .contact-label { position: absolute; left: 50px; top: 208px; font-size: 12px; font-weight: bold; color: var(--orange); }
  .contact-phone { position: absolute; left: 50px; top: 223px; font-size: 11.5px; color: var(--grey-light); letter-spacing: .3px; }

  .services { position: absolute; left: 32px; top: 262px; list-style: none; font-size: 16px; color: var(--grey); line-height: 18.5px; text-transform: uppercase; letter-spacing: .3px; }

  .photo { position: absolute; }
  .photo--park { left: 416px; top: 36px; width: 137px; height: 103px; background: linear-gradient(180deg, #8fb0d4 0%, #6d7f4e 55%, #a08a5a 100%); }
  .photo--field { left: 535px; top: 94px; width: 104px; height: 173px; background: linear-gradient(180deg, #c9d6e2 0%, #7a9a45 25%, #5f7d35 100%); }
  .photo--sky { left: 362px; top: 135px; width: 137px; height: 101px; background: linear-gradient(180deg, #7fa6d6 0%, #dfe6ee 50%, #6f6a45 100%); }
  .photo--hill { left: 455px; top: 228px; width: 116px; height: 87px; background: linear-gradient(180deg, #b7cde6 0%, #6f8a4a 45%, #8a7a4d 100%); }
</style>
</head>
<body>

  <section class="card card--dark card--front">
    <div class="wordmark">MEADOW PAWS</div>
    <div class="tagline">HAPPY HOUNDS</div>
    <div class="puppy-photo" role="img" aria-label="Photo of a puppy peeking over the bottom edge"></div>
    <div class="web-band">WWW.MEADOWPAWSDEMO.COM.AU</div>
  </section>

  <section class="card card--dark card--plain">
    <div class="wordmark">MEADOW PAWS</div>
    <div class="tagline">HAPPY HOUNDS</div>
    <div class="web-band">WWW.MEADOWPAWSDEMO.COM.AU</div>
  </section>

  <section class="card card--back">
    <div class="wordmark">MEADOW PAWS</div>
    <div class="tagline">HAPPY HOUNDS</div>

    <svg class="pointer" width="20" height="38" viewBox="0 0 20 38" aria-hidden="true">
      <polygon points="0,0 20,19 0,38" fill="var(--orange)"/>
    </svg>
    <div class="contact-name">Rua</div>
    <div class="contact-label">Tel:</div>
    <div class="contact-phone">0498307164</div>

    <ul class="services">
      <li>-Walking</li>
      <li>-Holiday stays</li>
      <li>-Onsite care</li>
      <li>-Training and behavioural consultations</li>
    </ul>

    <div class="photo photo--park" role="img" aria-label="Photo of dogs together in a park"></div>
    <div class="photo photo--field" role="img" aria-label="Photo of a brown dog walking across a grassy field"></div>
    <div class="photo photo--sky" role="img" aria-label="Photo of a fluffy dog against a cloudy sky"></div>
    <div class="photo photo--hill" role="img" aria-label="Photo of dogs on a hillside overlooking a valley"></div>

    <div class="web-band">WWW.MEADOWPAWSDEMO.COM.AU</div>
  </section>

</body>
</html>
```